HTML Email Blast design

We need an HTML email blast designed.
Uploaded files include:
- specs attached in file named brelton-works eblast specs.
- copy / content - word document
- logo

Here's an example of an eblast I really like:
https://quellbox.example/48213907-2b6e-4f1d-9c83-a7e5d2b1c4f903925817463

-

Industry/Entity Type

Finance

Font styles to use
Sans Serif

```html
<!DOCTYPE html>
<html lang="en">
<head>
<meta charset="utf-8">
<title>Kestrel REIT – Structured Finance</title>
<link rel="stylesheet" href="https://fonts.googleapis.com/css2?family=Open+Sans:wght@400;600;700&display=swap">
<style>
:root{
  --page-bg:#dcdcdc;
  --card-bg:#ffffff;
  --ink:#111111;
  --brand-blue:#1474d0;
  --rule-blue:#2b4b8c;
  --navy:#233563;
  --photo-a:#e9ecef;
  --photo-b:#d5dbe2;
  --map-blue:#2f86d6;
  --map-grey:#cfcfcf;
  --white:#ffffff;
}
*{margin:0;padding:0;box-sizing:border-box}
html,body{width:1200px;height:3094px;overflow:hidden}
body{background:var(--page-bg);font-family:"Open Sans",Arial,sans-serif;color:var(--ink);position:relative}
.card{position:absolute;left:71px;top:71px;width:1049px;height:2824px;background:var(--card-bg)}
.hero{position:absolute;left:71px;top:71px;width:1049px;height:286px;
  background:linear-gradient(180deg,var(--photo-a),var(--photo-b))}
.hero-rule{position:absolute;left:71px;top:356px;width:1049px;height:3px;background:var(--rule-blue)}
.brand{position:absolute;left:162px;top:188px;display:flex;align-items:center;gap:16px}
.brand-mark{width:40px;height:40px;background:var(--navy)}
.brand-name{font-size:44px;font-weight:700;color:var(--navy);letter-spacing:1px}
.btn{position:absolute;display:flex;align-items:center;justify-content:center;background:var(--brand-blue);
  color:var(--white);font-weight:600;text-decoration:none;box-shadow:0 3px 6px rgba(0,0,0,.25)}
.btn-header{left:759px;top:178px;width:255px;height:73px;font-size:38px}
.btn-footer{left:441px;top:2953px;width:311px;height:57px;font-size:34px;font-weight:400;box-shadow:none}
.abs{position:absolute}
.title{left:184px;top:408px;font-size:42px;font-weight:700}
.lead{left:184px;width:840px;font-size:24px;line-height:30px}
.divider{position:absolute;left:184px;width:823px;height:2px;background:var(--rule-blue)}
.section-head{position:absolute;left:160px;display:flex;align-items:center;height:56px}
.section-head svg{width:32px;height:56px;margin-right:7px}
.section-head h2{font-size:36px;font-weight:700;letter-spacing:.3px}
.list{position:absolute;list-style:none;font-size:23px;line-height:33px}
.list li{position:relative;padding-left:37px}
.list li::before{content:"";position:absolute;left:3px;top:13px;width:8px;height:8px;background:var(--ink);transform:rotate(45deg)}
.specs{left:202px;top:1559px;font-size:23px;line-height:28px}
.specs dt{font-weight:700}
.specs dd{margin-bottom:18px}
.stats{left:0;width:1190px;top:2110px;text-align:center;font-size:24px;font-weight:600}
.map{left:250px;top:2171px;width:703px;height:430px;
  background:linear-gradient(135deg,var(--map-blue) 0%,var(--map-blue) 55%,var(--map-grey) 100%)}
.about{left:180px;width:850px;font-size:26px;line-height:30px}
.footer{position:absolute;left:0;top:2895px;width:1200px;height:199px;background:var(--navy)}
.social{position:absolute;left:527px;top:3029px;display:flex;gap:16px}
.social span{width:22px;height:22px;border-radius:50%;background:var(--white)}
</style>
</head>
<body>
<div class="card"></div>
<div class="hero" role="img" aria-label="Faded photo of a senior living community building"></div>
<div class="hero-rule"></div>
<div class="brand"><span class="brand-mark"></span><span class="brand-name">Kestrel REIT</span></div>
<a class="btn btn-header" href="#">Contact Us!</a>

<h1 class="abs title">Need Financing? We’ve got it.</h1>
<p class="abs lead" style="top:473px">Challenging times demand adaptive measures. We're constantly thinking outside of the REIT box to develop creative financing solutions.</p>
<p class="abs lead" style="top:549px">Of course, we continue to offer our core NNN and JV structures. <b>But, did you know we also offer a variety of structured finance products?</b> These solutions provide a range of levers Kestrel can pull to help finance projects.</p>

<div class="divider" style="top:723px"></div>
<div class="section-head" style="top:781px"><svg viewBox="0 0 32 56"><polyline points="29,2 4,28 29,54" fill="none" stroke="var(--brand-blue)" stroke-width="4"/></svg><h2>BENEFITS OF STRUCTURED FINANCE:</h2></div>
<ul class="list" style="left:200px;top:864px;width:820px">
  <li>Provide liquidity through releasing “trapped” equity in properties</li>
  <li>Bridge maturing loans while waiting for the market to return to normal</li>
  <li>Fund construction for shovel-ready projects</li>
  <li>Fund existing projects where other investors have backed away</li>
  <li style="line-height:28px;margin-top:5px">Provide an exit plan for equity investors who may have their own liquidity needs</li>
</ul>

<div class="divider" style="top:1113px"></div>
<div class="section-head" style="top:1173px"><svg viewBox="0 0 32 56"><polyline points="29,2 4,28 29,54" fill="none" stroke="var(--brand-blue)" stroke-width="4"/></svg><h2>PRODUCTS INCLUDE:</h2></div>
<ul class="list" style="left:200px;top:1257px">
  <li>Mezzanine</li><li>Bridge</li><li>Unitranche Financing</li>
</ul>
<ul class="list" style="left:654px;top:1257px">
  <li>Preferred Equity</li><li>Construction Financing</li>
</ul>

<div class="divider" style="top:1413px"></div>
<div class="section-head" style="top:1473px"><svg viewBox="0 0 32 56"><polyline points="29,2 4,28 29,54" fill="none" stroke="var(--brand-blue)" stroke-width="4"/></svg><h2>PRODUCTS INCLUDE:</h2></div>
<dl class="abs specs">
  <dt>Transaction Size:</dt><dd>100$ - 2$ million</dd>
  <dt>Property Types:</dt><dd>Independent Living, Assisted Living, Memory Care, Skilled Nursing</dd>
  <dt>Locations:</dt><dd>Contiguous USA</dd>
  <dt>Financing Types:</dt><dd>NNN, JV, Mezzanine, Bridge, Construction, Unitranche, Preferred Equity</dd>
  <dt>Operators:</dt><dd>Regional, growth-oriented</dd>
</dl>

<div class="divider" style="top:1969px"></div>
<div class="section-head" style="top:2026px"><svg viewBox="0 0 32 56"><polyline points="29,2 4,28 29,54" fill="none" stroke="var(--brand-blue)" stroke-width="4"/></svg><h2>ABOUT KESTREL:</h2></div>
<p class="abs stats">+180 Investments | 27 States | 30 Operating Partners</p>
<div class="abs map" role="img" aria-label="Map of the contiguous United States with the 27 states where investments are held highlighted in blue"></div>
<p class="abs about" style="top:2641px">Shared success is based on partnership and alignment. Our business is about much more than real estate. It is about the operators who run the communities and the residents who call our buildings home.</p>
<p class="abs about" style="top:2754px">We focus on building strong, long-term relationships and work to align interests ensuring that all businesses are supported to create the best outcomes for all.</p>

<footer class="footer"></footer>
<a class="btn btn-footer" href="#">Contact Us Today</a>
<div class="social" aria-label="Social links"><span></span><span></span><span></span><span></span></div>
</body>
</html>
```